Solar energy proposal for homeowners

I am providing households with solar energy proposals, and I need a high-quality brochure that is packaged cleverly to attract the homeowner's attention. Take a look at the one page solar brochure that I have included to get an idea of text and content.

Target Market(s)

Residential Homeowners

Industry/Entity Type

Solar

Requirements
Must have
• High quality document

```html
<!DOCTYPE html>
<html lang="en">
<head>
<meta charset="utf-8">
<title>Brightvale Energy – Solar For $0 Down</title>
<link href="https://fonts.googleapis.com/css2?family=Poppins:ital,wght@0,400;0,500;0,600;0,700;0,800;1,500;1,700&display=swap" rel="stylesheet">
<style>
  :root {
    --deep: #063a4c;
    --teal-dark: #0a4a5a;
    --teal-mid: #0d5a70;
    --cyan: #00b5cc;
    --blue: #0097d6;
    --green: #9dd62a;
    --white: #ffffff;
    --ink: #0b2a3a;
  }
  * { margin: 0; padding: 0; box-sizing: border-box; }
  html, body { width: 866px; height: 1200px; overflow: hidden; background: #e9eef0; }
  body { font-family: 'Poppins', sans-serif; color: var(--white); }

  .flyer {
    position: relative;
    width: 866px; height: 1200px; overflow: hidden;
    background:
      radial-gradient(ellipse at 0% 0%, #126a5a 0%, transparent 45%),
      linear-gradient(160deg, var(--teal-dark) 0%, #0b4f66 45%, var(--teal-mid) 100%);
  }

  .headline { position: absolute; left: 55px; top: 40px; font-weight: 700; font-size: 58px; line-height: 1.08; letter-spacing: -0.5px; }
  .tagline {
    position: absolute; left: 55px; top: 184px; font-weight: 700; font-size: 52px; line-height: 1.22; letter-spacing: -0.5px;
    background: linear-gradient(90deg, var(--blue) 0%, var(--cyan) 45%, var(--green) 100%);
    -webkit-background-clip: text; background-clip: text; color: transparent;
  }
  .subline { position: absolute; left: 55px; top: 326px; font-weight: 500; font-size: 25px; line-height: 1.25; }

  .about {
    position: absolute; left: 57px; top: 419px; width: 305px; height: 420px;
    background: var(--cyan); border-radius: 8px 8px 0 0; padding: 38px 18px 0 21px;
  }
  .about h2 { color: #0a0a0a; font-size: 23px; font-weight: 700; margin-bottom: 6px; }
  .about p { font-size: 16.2px; line-height: 1.22; font-weight: 500; }

  .house-photo { position: absolute; left: 0; top: 720px; width: 545px; height: 480px; }

  .brand { position: absolute; left: 491px; top: 62px; display: flex; align-items: center; gap: 12px; }
  .brand-mark { width: 40px; height: 40px; background: var(--cyan); }
  .brand-name { font-size: 30px; font-weight: 500; color: var(--cyan); letter-spacing: 0.2px; }

  .why-pill {
    position: absolute; left: 432px; top: 181px; width: 386px; height: 48px;
    background: var(--green); border-radius: 24px; color: var(--ink);
    font-size: 22px; font-weight: 700; padding-left: 32px; line-height: 48px;
  }
  .why-list { position: absolute; left: 432px; top: 243px; width: 386px; list-style: none; }
  .why-list li {
    height: 36px; margin-bottom: 4px; border: 1.5px solid var(--green); border-radius: 18px;
    background: rgba(4, 45, 66, 0.55); display: flex; align-items: center; font-size: 16.5px; font-weight: 500;
  }
  .why-list svg { width: 20px; height: 20px; margin: 0 23px 0 12px; }

  .service-title { position: absolute; left: 434px; top: 514px; font-size: 23px; font-weight: 700; color: var(--green); }

  .card {
    position: absolute; width: 186px; height: 157px; border-radius: 10px;
    transform: skewX(-4deg); padding: 14px 12px 0 18px;
  }
  .card.blue { background: var(--blue); }
  .card.cyan { background: var(--cyan); }
  .card h3 { color: var(--ink); font-size: 14.5px; font-weight: 700; line-height: 1.2; max-width: 110px; margin-bottom: 2px; }
  .card p { font-size: 13px; line-height: 1.24; font-weight: 500; }
  .card.italic h3, .card.italic p { font-style: italic; }
  .card-icon { position: absolute; right: 12px; top: 10px; width: 30px; height: 30px; }
  .card-1 { left: 432px; top: 559px; }
  .card-2 { left: 620px; top: 559px; }
  .card-3 { left: 432px; top: 727px; }
  .card-4 { left: 620px; top: 727px; }
  .card-4 h3 { margin-top: 14px; margin-bottom: 10px; max-width: 130px; }

  .contact-title { position: absolute; left: 550px; top: 955px; font-size: 29px; font-weight: 700; }
  .contact-row {
    position: absolute; left: 550px; width: 316px; height: 48px; border-radius: 24px 0 0 24px;
    display: flex; align-items: center; padding-left: 8px; font-weight: 600;
  }
  .contact-row svg { width: 26px; height: 26px; margin-right: 8px; flex: none; }
  .contact-row.phone { top: 1002px; background: var(--green); color: var(--ink); font-size: 27px; font-weight: 700; }
  .contact-row.address, .contact-row.web { border: 2px solid var(--green); border-right: none; background: var(--deep); font-size: 16px; }
  .contact-row.address { top: 1059px; }
  .contact-row.web { top: 1117px; }
</style>
</head>
<body>
<main class="flyer">
  <h1 class="headline">Solar For<br>$0 Down.</h1>
  <p class="tagline">No Liens.<br>No Kidding.</p>
  <p class="subline">Power Your Future with<br>Brightvale Energy</p>

  <section class="about">
    <h2>About Us</h2>
    <p>At Brightvale Energy, our mission is to make solar simple and accessible for everyone. No high-pressure sales—just the information you need to make a smart choice. With our solar rental program, you can lower your monthly energy costs and pay less than your current electricity bill.</p>
  </section>

  <svg class="house-photo" viewBox="0 0 545 480" role="img" aria-label="Photo of a white brick house with blue solar panels on its roof">
    <defs>
      <linearGradient id="roofPanels" x1="0" y1="0" x2="1" y2="1">
        <stop offset="0" stop-color="#3a6fd0"/>
        <stop offset="0.55" stop-color="#1e3f8a"/>
        <stop offset="1" stop-color="#d9dde0"/>
      </linearGradient>
    </defs>
    <polygon points="0,0 230,40 400,120 545,140 545,480 0,480" fill="url(#roofPanels)"/>
  </svg>

  <div class="brand">
    <span class="brand-mark"></span>
    <span class="brand-name">Brightvale Energy</span>
  </div>

  <div class="why-pill">Why Choose Us?</div>
  <ul class="why-list">
    <li><svg viewBox="0 0 20 20"><circle cx="10" cy="10" r="9" fill="none" stroke="#00b5cc" stroke-width="2"/><line x1="4" y1="16" x2="16" y2="4" stroke="#fff" stroke-width="2"/></svg>No financing</li>
    <li><svg viewBox="0 0 20 20"><circle cx="10" cy="10" r="9" fill="none" stroke="#00b5cc" stroke-width="2"/><line x1="4" y1="16" x2="16" y2="4" stroke="#fff" stroke-width="2"/></svg>No liens</li>
    <li><svg viewBox="0 0 20 20"><circle cx="10" cy="10" r="9" fill="none" stroke="#00b5cc" stroke-width="2"/><line x1="4" y1="16" x2="16" y2="4" stroke="#fff" stroke-width="2"/></svg>No down payment</li>
    <li><svg viewBox="0 0 20 20"><circle cx="10" cy="10" r="9" fill="none" stroke="#00b5cc" stroke-width="2"/><line x1="4" y1="16" x2="16" y2="4" stroke="#fff" stroke-width="2"/></svg>No insurance costs</li>
    <li><svg viewBox="0 0 20 20"><circle cx="10" cy="10" r="9" fill="none" stroke="#00b5cc" stroke-width="2"/><line x1="4" y1="16" x2="16" y2="4" stroke="#fff" stroke-width="2"/></svg>No long-term commitment</li>
    <li><svg viewBox="0 0 20 20"><circle cx="10" cy="10" r="9" fill="none" stroke="#00b5cc" stroke-width="2"/><line x1="4" y1="16" x2="16" y2="4" stroke="#fff" stroke-width="2"/></svg>No maintenance costs</li>
  </ul>

  <h2 class="service-title">Our Best Service</h2>

  <article class="card blue card-1">
    <svg class="card-icon" viewBox="0 0 30 30"><circle cx="18" cy="10" r="7" fill="none" stroke="#0b2a3a" stroke-width="1.5"/><text x="18" y="14" font-size="10" text-anchor="middle" fill="#0b2a3a" font-family="Poppins, sans-serif">$</text><path d="M2 24 L10 20 L20 21 L27 17" fill="none" stroke="#0b2a3a" stroke-width="1.5"/></svg>
    <h3>Affordable &amp; Transparent</h3>
    <p>Simple pricing, no hidden fees and a fixed monthly rate lower than typical energy bills.</p>
  </article>
  <article class="card cyan card-2">
    <svg class="card-icon" viewBox="0 0 30 30"><circle cx="15" cy="15" r="11" fill="none" stroke="#0b2a3a" stroke-width="2" stroke-dasharray="4 2"/><circle cx="15" cy="15" r="6" fill="none" stroke="#0b2a3a" stroke-width="1.5"/><path d="M12 15 l2 2 l4 -4" fill="none" stroke="#0b2a3a" stroke-width="1.5"/></svg>
    <h3>Expert Installation</h3>
    <p>Certified professionals handle installation, maintenance, and repairs end to end.</p>
  </article>
  <article class="card cyan italic card-3">
    <svg class="card-icon" viewBox="0 0 30 30"><circle cx="11" cy="15" r="7" fill="none" stroke="#0b2a3a" stroke-width="2" stroke-dasharray="3 2"/><circle cx="21" cy="20" r="6" fill="none" stroke="#0b2a3a" stroke-width="1.5"/><path d="M18 20 l2 2 l4 -4" fill="none" stroke="#0b2a3a" stroke-width="1.5"/></svg>
    <h3>Local Expertise</h3>
    <p>Florida-based team that understands the needs of Orlando and statewide homeowners.</p>
  </article>
  <article class="card blue italic card-4">
    <svg class="card-icon" viewBox="0 0 30 30"><path d="M15 4 L25 22 L5 22 Z" fill="none" stroke="#0b2a3a" stroke-width="1.5"/><path d="M12 6 l3 -2 l1 4 M26 19 l-1 3 l-4 -1 M6 19 l-1 3 l4 0" fill="none" stroke="#0b2a3a" stroke-width="1.5"/></svg>
    <h3>Eco-Friendly</h3>
    <p>Clean, renewable solar energy that helps reduce your carbon footprint.</p>
  </article>

  <h2 class="contact-title">Contact Us Now!</h2>
  <div class="contact-row phone">
    <svg viewBox="0 0 26 26"><circle cx="13" cy="13" r="13" fill="#0b2a3a"/><path d="M9 7 l3 0 l1 4 l-2 1 q1 3 4 4 l1 -2 l4 1 l0 3 q-8 1 -11 -11 z" fill="#fff"/></svg>
    (555) 014-2290
  </div>
  <div class="contact-row address">
    <svg viewBox="0 0 26 26"><circle cx="13" cy="13" r="13" fill="#9dd62a"/><path d="M13 6 a5 5 0 0 1 5 5 c0 4 -5 9 -5 9 s-5 -5 -5 -9 a5 5 0 0 1 5 -5 z" fill="#fff"/><circle cx="13" cy="11" r="2" fill="#9dd62a"/></svg>
    123 Anywhere St., Any City
  </div>
  <div class="contact-row web">
    <svg viewBox="0 0 26 26"><circle cx="13" cy="13" r="13" fill="#9dd62a"/><circle cx="13" cy="13" r="7" fill="none" stroke="#fff" stroke-width="1.5"/><ellipse cx="13" cy="13" rx="3" ry="7" fill="none" stroke="#fff" stroke-width="1.2"/><line x1="6" y1="13" x2="20" y2="13" stroke="#fff" stroke-width="1.2"/></svg>
    www.brightvaleenergy.com
  </div>
</main>
</body>
</html>
```